Business Card Design

Electrical Contracting buisness
need a buisness card relating to that buisness

Reason: Just need to discuss with partner

Industry/Entity Type

Business

Contact Information for Business Card

Colin Harbage Electrical
0417 562 983
colinharbage7@mailvessel.com
REC 48761

```html
<!DOCTYPE html>
<html lang="en">
<head>
<meta charset="utf-8">
<title>Colin Harbage Electrical – Business Card</title>
<link rel="stylesheet" href="https://fonts.googleapis.com/css2?family=Saira+Condensed:wght@500;600&family=Saira:wght@400;600&display=swap">
<style>
  :root {
    --bg: #e9e6e2;
    --card: #ffffff;
    --ink: #2f2f33;
    --blue-deep: #1d4fa8;
    --blue: #2b7fd6;
    --blue-light: #3f9be6;
    --orange: #f0612b;
    --orange-light: #f7923a;
    --on-blue: #ffffff;
  }
  * { margin: 0; padding: 0; box-sizing: border-box; }
  html, body { width: 1200px; height: 675px; overflow: hidden; background: var(--bg); }
  .stage { position: relative; width: 1200px; height: 675px; }
  .card {
    position: absolute; left: 100px; top: 52px; width: 1000px; height: 572px;
    background: var(--card); overflow: hidden;
    box-shadow: 0 10px 30px rgba(0,0,0,0.18);
  }
  .card-shapes { position: absolute; inset: 0; }
  .brand {
    position: absolute; left: 600px; top: 120px;
    display: flex; align-items: center; gap: 18px;
  }
  .brand-dot { width: 62px; height: 62px; border-radius: 50%; background: var(--orange); }
  .brand-name {
    font-family: 'Saira', sans-serif; font-weight: 600; font-size: 34px;
    line-height: 1.05; letter-spacing: 2px; color: var(--blue-deep); text-transform: uppercase;
  }
  .holder { position: absolute; left: 70px; top: 212px; }
  .holder-name {
    font-family: 'Saira Condensed', sans-serif; font-weight: 600; font-size: 64px;
    color: var(--ink); letter-spacing: 1px; line-height: 1;
  }
  .holder-role {
    font-family: 'Saira', sans-serif; font-size: 19px; letter-spacing: 3px;
    color: var(--ink); margin-top: 12px;
  }
  .contact {
    position: absolute; font-family: 'Saira', sans-serif; font-size: 19px;
    color: var(--on-blue); line-height: 1.35; letter-spacing: 1px;
  }
  .contact svg { display: block; margin-bottom: 10px; }
  .contact-address { left: 60px; top: 432px; }
  .contact-phone { left: 400px; top: 408px; text-align: center; }
  .contact-phone svg { margin: 0 auto 10px; }
  .contact-web { right: 56px; top: 372px; text-align: center; font-size: 18px; letter-spacing: 0.5px; }
  .contact-web svg { margin: 0 auto 10px; }
</style>
</head>
<body>
<main class="stage">
  <section class="card" aria-label="Business card">
    <svg class="card-shapes" width="1000" height="572" viewBox="0 0 1000 572" aria-hidden="true">
      <defs>
        <linearGradient id="blueBand" x1="0" y1="0" x2="1" y2="0">
          <stop offset="0" stop-color="#1d4fa8"/>
          <stop offset="0.5" stop-color="#2b7fd6"/>
          <stop offset="1" stop-color="#1d4fa8"/>
        </linearGradient>
        <linearGradient id="orangeBand" x1="0" y1="0" x2="1" y2="0">
          <stop offset="0" stop-color="#f0612b"/>
          <stop offset="1" stop-color="#f7923a"/>
        </linearGradient>
      </defs>
      <path class="swoosh-orange" d="M0 46 C180 40 420 20 640 0 L700 0 C470 34 220 66 0 70 Z" fill="url(#orangeBand)"/>
      <path class="swoosh-blue" d="M0 0 L640 0 C420 20 180 40 0 46 Z" fill="url(#blueBand)"/>
      <path class="band-orange" d="M0 402 C300 388 650 360 1000 318 L1000 572 L0 572 Z" fill="url(#orangeBand)"/>
      <path class="band-blue" d="M0 414 C300 400 650 374 1000 332 L1000 572 L0 572 Z" fill="url(#blueBand)"/>
    </svg>

    <div class="brand">
      <span class="brand-dot"></span>
      <p class="brand-name">Colin Harbage<br>Electrical</p>
    </div>

    <div class="holder">
      <h1 class="holder-name">DEAN MORRELL</h1>
      <p class="holder-role">GENERAL MANAGER</p>
    </div>

    <div class="contact contact-address">
      <svg width="20" height="26" viewBox="0 0 20 26"><path d="M10 0C4.5 0 0 4.4 0 9.8 0 17 10 26 10 26s10-9 10-16.2C20 4.4 15.5 0 10 0Zm0 14a4 4 0 1 1 0-8 4 4 0 0 1 0 8Z" fill="#fff"/></svg>
      14 Kessel Road,<br>Unit 3 Parkfield
    </div>

    <div class="contact contact-phone">
      <svg width="22" height="22" viewBox="0 0 24 24"><path d="M6.6 10.8a15 15 0 0 0 6.6 6.6l2.2-2.2c.3-.3.7-.4 1-.2 1.1.4 2.3.6 3.6.6.6 0 1 .4 1 1V20c0 .6-.4 1-1 1A17 17 0 0 1 3 4c0-.6.4-1 1-1h3.5c.6 0 1 .4 1 1 0 1.3.2 2.5.6 3.6.1.3 0 .7-.2 1l-2.3 2.2Z" fill="#fff"/></svg>
      0417 562 983<br>REC 48761
    </div>

    <div class="contact contact-web">
      <svg width="24" height="24" viewBox="0 0 24 24" fill="none" stroke="#fff" stroke-width="1.6"><circle cx="12" cy="12" r="10"/><ellipse cx="12" cy="12" rx="4.5" ry="10"/><path d="M2 12h20M4 6.5h16M4 17.5h16"/></svg>
      colinharbage7@mailvessel.com<br>colinharbage-elec.com.au
    </div>
  </section>
</main>
</body>
</html>
```